Offshore Survey Ship Technical Specification Sheet

We are a provider of specialist survey vessels (ships) to the worldwide oil, gas, telecommunications and renewable energy sectors.

We would like to replace our existing specification sheets that briefly outline the Company information and provide a table of the technical specifications of the ships and survey equipment.

The final design should be two stand-alone documents that are obviously from the same source. The design should be an attractive presentation of each of our ships.

The final deliverable should be provided in an editable format because the vessel and equipment specifications change occasionally and the specification sheets will need to be amended to reflect the changes.

The brochure/specification sheet should cover both sides of a single ISO A4 size sheet.

Our company is based in Iceland and the colour scheme of our vessels reflect the Icelandic flag; blue, red and white.

The ships can be seen on our website.... www.skarvel.is

The existing specification sheets are available here.... http://www.skarvel.is/en/equipment/vessels

The technical specifications and details of equipment shall be provided in a spreadsheet but will be similar in content to the existing spec. sheets.

Images of the vessels are available and will be uploaded along with the Company logo.

If you need any other images, drawings or alternaitve formats (e.g. .eps logo) to support your design ideas then please do not hesitate to contact us.
Updates

Hi

The specification tables have been uploaded.

There are two tabs; one for the ship's equipment and another for the survey equipment.

Many thanks in advance...

Reason: We are very busy with our other operations today.

Hello All

I have uploaded some text in the document 'Brochure Text.doc'.

There are three sections to be added to the designs...

1 .  General text and correct address to be included on both specification sheets
2 .  Specific text for the MV Ostrava only
3.  Specific text for the MV Halvard only

We were very busy yesterday and will be again today.  I will try and send comments during today.

Thank You.

Target Market(s)

worldwide oil, gas, telecommunications and renewable energy operators.

Industry/Entity Type

Telecommunications

Requirements
Must have
• Two sides of A4 for each specification sheet - a design of 4 x A4 sides in total (2 specification sheets).

Table of equipment specifications.

```html
<!DOCTYPE html>
<html lang="en">
<head>
<meta charset="utf-8">
<title>Skarvel – Halvard SK 27 Specification Sheet</title>
<link href="https://fonts.googleapis.com/css2?family=Source+Sans+3:wght@400;600;700&family=PT+Sans+Narrow:wght@700&display=swap" rel="stylesheet">
<style>
  :root{
    --brand-blue:#1d5aa3;
    --heading-blue:#1c5296;
    --band-blue:#1d4e8e;
    --header-grey:#e8e9eb;
    --sheet-bg:#f1f1f2;
    --panel:#ffffff;
    --text:#1f1f1f;
    --label:#3a3a3a;
  }
  *{box-sizing:border-box;margin:0;padding:0}
  html,body{width:916px;height:1200px;overflow:hidden;background:var(--sheet-bg)}
  body{font-family:"Source Sans 3",Arial,sans-serif;color:var(--text);position:relative}

  .sheet-header{position:absolute;left:0;top:0;width:916px;height:194px;background:var(--header-grey);border-bottom:4px solid var(--band-blue)}
  .brand{position:absolute;left:27px;top:38px;display:flex;align-items:center;gap:20px}
  .brand-square{width:55px;height:76px;background:var(--brand-blue)}
  .brand-name{font-size:84px;font-weight:400;color:var(--brand-blue);line-height:1;letter-spacing:-1px}

  .contact{position:absolute;left:672px;top:46px;font-size:14px;font-weight:700;line-height:24.5px;color:#222}
  .contact li{list-style:none;display:flex;align-items:center;gap:5px}
  .contact svg{width:12px;height:12px;fill:#222}
  .contact .indent{padding-left:17px}

  .panel{position:absolute;background:var(--panel);box-shadow:0 2px 6px rgba(0,0,0,.35)}
  .panel-left{left:22px;top:197px;width:427px;height:907px;z-index:2}
  .panel-right{left:467px;top:197px;width:422px;height:822px}

  .section-title{position:absolute;font-family:"PT Sans Narrow","Arial Narrow",sans-serif;font-weight:700;font-size:25px;color:var(--heading-blue);line-height:1}
  .spec{position:absolute;list-style:none;font-size:15px;line-height:27px}
  .spec li{display:flex;white-space:nowrap}
  .spec .k{flex:0 0 auto}
  .spec.bold{font-weight:700}
  .spec.left .k{width:238px;color:var(--label)}
  .spec.left .v{font-weight:600}
  .spec.safety .k{width:202px;font-weight:700}
  .spec.safety .v{font-weight:700}
  .spec.engine .k{width:215px}

  .footer-band{position:absolute;left:0;top:1113px;width:415px;height:87px;background:var(--band-blue);z-index:1}
  .badge{position:absolute;background:#fff;top:17px;height:62px}
  .badge-one{left:41px;width:183px}
  .badge-two{left:236px;width:130px}

  .vessel-photo{position:absolute;left:415px;top:1019px;width:501px;height:181px;
    background:linear-gradient(180deg,#d6dee8 0%,#c4ccd8 30%,#9aa6b6 52%,#7f93a8 62%,#6f8ca6 100%)}
</style>
</head>
<body>
  <header class="sheet-header">
    <div class="brand">
      <div class="brand-square"></div>
      <div class="brand-name">Skarvel</div>
    </div>
    <ul class="contact">
      <li>Tel: +354 555 0140</li>
      <li>Fax: +354 555 0141</li>
      <li><svg viewBox="0 0 12 12"><path d="M1 3h10v6H1z" fill="none" stroke="#222" stroke-width="1.4"/><path d="M1 3l5 4 5-4" fill="none" stroke="#222" stroke-width="1.4"/></svg>: webmaster@skarvel.is</li>
      <li><svg viewBox="0 0 12 12"><path d="M6 1L1 6h1.5v5h3V8h1v3h3V6H11z"/></svg>: Iceland Office, Strandgata 14</li>
      <li class="indent">735 Fjardvik</li>
    </ul>
  </header>

  <section class="panel panel-left">
    <h2 class="section-title" style="left:18px;top:19px">Vessel Details</h2>
    <ul class="spec left" style="left:18px;top:54px">
      <li><span class="k">Name</span><span class="v">Halvard SK 27</span></li>
      <li><span class="k">IMO No.</span><span class="v">7519832</span></li>
      <li><span class="k">MMSI No.</span><span class="v">251608230</span></li>
      <li><span class="k">Call Sign</span><span class="v">TFQR</span></li>
      <li><span class="k">Flag</span><span class="v">Icelandic</span></li>
      <li><span class="k">Classification (type)</span><span class="v">Multi-Purpose DP</span></li>
      <li><span class="k"></span><span class="v" style="padding-left:12px">1Survey Vessel</span></li>
      <li><span class="k">Year built</span><span class="v">1976</span></li>
      <li><span class="k">Last overhaul/refit</span><span class="v">2008/20137</span></li>
      <li><span class="k">Length overall</span><span class="v">49.85m</span></li>
      <li><span class="k">Beam</span><span class="v">9.5m</span></li>
      <li><span class="k">Draught</span><span class="v">6.2m</span></li>
      <li><span class="k">Tonnage</span><span class="v">1078.63 gross tonnes</span></li>
      <li><span class="k">Operating Range</span><span class="v">23460 nautical miles</span></li>
      <li><span class="k">Main/primary Deck Space</span><span class="v">37m2</span></li>
      <li><span class="k">Other/secondary Deck Space</span><span class="v">72m2</span></li>
    </ul>

    <h2 class="section-title" style="left:18px;top:493px">Capacities</h2>
    <ul class="spec left bold" style="left:18px;top:529px">
      <li><span class="k">Fuel</span><span class="v">468.1 m3</span></li>
      <li><span class="k">Fuel consumption</span><span class="v">2.5-3.0 m3/day (survey)</span></li>
      <li><span class="k">Water</span><span class="v">53 m3</span></li>
      <li><span class="k">Water Making</span><span class="v">15 m3/day</span></li>
      <li><span class="k">Endurance</span><span class="v">85 days</span></li>
    </ul>

    <h2 class="section-title" style="left:18px;top:676px">Accommodation Details</h2>
    <ul class="spec left bold" style="left:18px;top:714px">
      <li><span class="k">Total Berths</span><span class="v">35</span></li>
      <li><span class="k">Total Cabins</span><span class="v">22 + Hospital</span></li>
      <li><span class="k">No. Rec Rooms</span><span class="v">1</span></li>
      <li><span class="k">No. Gyms</span><span class="v">1</span></li>
      <li><span class="k">Online Survey Room</span><span class="v">23m2</span></li>
      <li><span class="k">Offline Survey Room</span><span class="v">14m2</span></li>
      <li><span class="k">Conference Room</span><span class="v">23m2</span></li>
    </ul>
  </section>

  <section class="panel panel-right">
    <h2 class="section-title" style="left:28px;top:21px">Safety</h2>
    <ul class="spec safety" style="left:28px;top:59px">
      <li><span class="k">Rescue / MOB Boat</span><span class="v">Kelda</span></li>
      <li><span class="k"></span><span class="v">25 HP</span></li>
      <li><span class="k"></span><span class="v">6 persons capacity</span></li>
      <li><span class="k">Life Rafts</span><span class="v">4 x Total</span></li>
      <li><span class="k"></span><span class="v">70 persons total capacity</span></li>
      <li><span class="k"></span><span class="v">2 x 10 persons capacity</span></li>
      <li><span class="k"></span><span class="v">2 x 25 persons capacity</span></li>
      <li><span class="k">Survival Suits</span><span class="v">35</span></li>
      <li><span class="k">Life Jackets</span><span class="v">42</span></li>
      <li><span class="k">Work Vest</span><span class="v">7</span></li>
      <li><span class="k">Emergency radios/Beacons</span><span class="v">3 x Vardi VR 2740</span></li>
      <li><span class="k">MOB System</span><span class="v">0.75 tonne davit capacity</span></li>
    </ul>

    <h2 class="section-title" style="left:28px;top:396px">Engine and Machinery</h2>
    <ul class="spec engine" style="left:23px;top:434px">
      <li><span class="k">Main Engine Model</span><span class="v">ORKA 6R 24-30</span></li>
      <li><span class="k">Main Engine Power</span><span class="v">1800 HP</span></li>
      <li><span class="k"></span><span class="v">1320 kW</span></li>
      <li><span class="k">Bollard Pull</span><span class="v">28 tonnes</span></li>
      <li><span class="k">Aux Engine 1 Model</span><span class="v">Brenner BX6 712T</span></li>
      <li><span class="k">Aux Engine 1 Power</span><span class="v">550 HP</span></li>
      <li><span class="k"></span><span class="v">400 kW</span></li>
      <li><span class="k">Aux Engine 2 Model</span><span class="v">Sokai 4KT-HM</span></li>
      <li><span class="k">Aux Engine 2 Power</span><span class="v">580 HP</span></li>
      <li><span class="k"></span><span class="v">438 kW</span></li>
      <li><span class="k">Bow Thruster Power</span><span class="v">330 kW</span></li>
      <li><span class="k">Stern Thruster Power</span><span class="v">257 kW</span></li>
      <li><span class="k">Max Speed</span><span class="v">12 kts</span></li>
      <li><span class="k">Cruising Speed</span><span class="v">11.5 kts</span></li>
    </ul>
  </section>

  <div class="vessel-photo" role="img" aria-label="Photograph of two red, white and blue survey vessels on a fjord with snow-capped mountains behind"></div>

  <footer class="footer-band">
    <div class="badge badge-one" aria-label="Supplier registration badge"></div>
    <div class="badge badge-two" aria-label="Industry association membership badge"></div>
  </footer>
</body>
</html>
```